Onboarding Infographic/brochure

We are a small criminal defense firm looking to create some sort of infographic or brochure that we can onboard new clients with. We are currently sending it out via email but want something a bit cooler and fun to send to clients. The information is:

A Few Quick Rules

We are here to help each step of the way. While questions are never discouraged, this letter will answer some of the most common ones we get asked.

Communications

As a client, you should always be in the loop. While we will try to respond to questions as quickly as possible, sometimes we are unable to respond right away. Do not worry - we promise to get back to you soon. Some questions might take some time to research, and a correct answer is better than a quick one.

Appointments

One of the benefits of having an attorney is the ability to discuss your case outside of court, minus the stress and headaches. If you need an appointment, please contact the office.

Appointments must be scheduled in advance. We do not want you to make a special trip to the office only to learn that we are in court or otherwise unavailable.

Jail Visits

If your family member is currently in jail, we take that very seriously. We will visit your loved one and introduce ourselves. While the case is ongoing, we ask that a family member be designated a “contact” person so that messages can be relayed quickly. Never discuss the facts of the case over the phone with someone who is in jail. Jail calls are recorded and we have seen too many cases go south based on remarks made over recorded lines.

Police Reports and Discovery

We will do our best to provide you with copies of everything we receive on your case. Most information will be emailed, so please keep your email address up to date.

Changes in Contact Information

If you move or change numbers during the case, please let us know. It is difficult to help if we are unable to reach you, and helping you is why we are here.

Court Appearances

Cases do not get resolved as quickly as they do on television. Expect there to be several hearings in your case and it may be necessary for you to attend one or more of them. If a hearing is set, you will receive notice of the date and time of each hearing.

Billing and Collections

We understand that this investment was a huge decision for you. As we focus on providing the best representation, we will need for you to stay on schedule with any payment arrangements agreed to at the time of your initial consultation.

Again, thank you for your trust in us. We look forward to getting a fantastic outcome on your case.

Target Market(s)

Criminal defense clients and their families

Industry/Entity Type

Legal

Font styles to use
Serif

Requirements
Must have
• Must incorporate all of the rules we email out. Would like diagrams, images or pictures
Nice to have
• We attached a Welcome brochure. Not sure I want it to look super similar, hence the request for infographic.

```html
<!DOCTYPE html>
<html lang="en">
<head>
<meta charset="utf-8">
<title>Client Onboarding Guide</title>
<link href="https://fonts.googleapis.com/css2?family=Barlow:wght@400&family=Montserrat:wght@500&display=swap" rel="stylesheet">
<style>
  :root{
    --page:#ffffff;
    --tile:#f1f1f1;
    --rules:#dabd4b;
    --comms:#dca250;
    --appts:#57b09b;
    --jail:#8cc496;
    --reports:#7d8d9c;
    --contact:#5b6f82;
    --court:#6a98d6;
    --billing:#3172c6;
    --art-light:#5d9be0;
    --art-dark:#1352b8;
    --ink:#ffffff;
  }
  *{box-sizing:border-box;margin:0;padding:0}
  html,body{width:704px;height:1200px;overflow:hidden;background:var(--page)}
  .guide{position:absolute;left:81px;top:65px;width:541px}
  .step{display:flex;height:133.5px}
  .step--flip{flex-direction:row-reverse}
  .step__icon{width:134px;flex:none;background:var(--tile);display:flex;align-items:center;justify-content:center}
  .step__art{width:82px;height:76px;border-radius:14px;background:linear-gradient(135deg,var(--art-light),var(--art-dark));opacity:.9}
  .step__panel{position:relative;flex:1;color:var(--ink);padding:17px 25px 0 34px}
  .step--flip .step__panel{padding:15px 28px 0 26px}
  .step__panel::before{content:"";position:absolute;top:29px;left:0;border-style:solid;border-width:12px 0 12px 13px;border-color:transparent transparent transparent var(--tile)}
  .step--flip .step__panel::before{left:auto;right:0;border-width:12px 13px 12px 0;border-color:transparent var(--tile) transparent transparent}
  .step__title{font-family:"Barlow",sans-serif;font-weight:400;font-size:20px;line-height:24px;margin-bottom:7px;white-space:nowrap}
  .step__num{display:inline-block;margin:0 12px 0 4px}
  .step--flip .step__num{margin-left:0}
  .step__text{font-family:"Montserrat",sans-serif;font-weight:500;font-size:8.8px;line-height:10.7px;letter-spacing:-0.22px;text-align:justify;hyphens:manual}
  .step--rules .step__text,.step--reports .step__text,.step--contact .step__text,.step--billing .step__text{text-align:left}
  .step--rules .step__panel{background:var(--rules)}
  .step--rules .step__text{margin-top:13px}
  .step--comms .step__panel{background:var(--comms)}
  .step--appts .step__panel{background:var(--appts);padding-left:23px;padding-right:14px}
  .step--jail .step__panel{background:var(--jail)}
  .step--reports .step__panel{background:var(--reports)}
  .step--contact .step__panel{background:var(--contact)}
  .step--court .step__panel{background:var(--court)}
  .step--billing .step__panel{background:var(--billing)}
  .step--appts .step__title,.step--reports .step__title,.step--court .step__title{margin-top:6px}
  .step--contact .step__title,.step--billing .step__title{margin-top:12px}
</style>
</head>
<body>
<main class="guide">

  <section class="step step--rules">
    <div class="step__icon"><div class="step__art" role="img" aria-label="Envelope with a question mark badge"></div></div>
    <div class="step__panel">
      <h2 class="step__title"><span class="step__num">01</span>A Few Quick Rules</h2>
      <div class="step__text"><p>We are here to help each step of the way. While questions are never discour&shy;aged, this letter will answer some of the most common ones we get asked.</p></div>
    </div>
  </section>

  <section class="step step--comms step--flip">
    <div class="step__icon"><div class="step__art" role="img" aria-label="Speech bubble"></div></div>
    <div class="step__panel">
      <h2 class="step__title"><span class="step__num">02</span>Communications</h2>
      <div class="step__text"><p>As a client, you should always be in the loop. While we will try to respond to questions as quickly as possible, sometimes we are unable to respond right away. Do not worry - we promise to get back to you soon. Some questions might take some time to research, and a correct answer is better than a quick one.</p></div>
    </div>
  </section>

  <section class="step step--appts">
    <div class="step__icon"><div class="step__art" role="img" aria-label="Calendar with a marked day"></div></div>
    <div class="step__panel">
      <h2 class="step__title"><span class="step__num">03</span>Appointments</h2>
      <div class="step__text">
        <p>One of the benefits of having an attorney is the ability to discuss your case out&shy;side of court, minus the stress and headaches. If you need an appointment, please contact the office.</p>
        <p>Appointments must be scheduled in advance. We do not want you to make a spe&shy;cial trip to the office only to learn that we are in court or otherwise unavailable.</p>
      </div>
    </div>
  </section>

  <section class="step step--jail step--flip">
    <div class="step__icon"><div class="step__art" role="img" aria-label="Locked jail bars"></div></div>
    <div class="step__panel">
      <h2 class="step__title"><span class="step__num">04</span>Jail Visits</h2>
      <div class="step__text"><p>If your family member is currently in jail, we take that very seriously. We will visit your loved one and introduce ourselves. While the case is ongoing, we ask that a family member be designated a “contact” person so that messages can be relayed quickly. Never discuss the facts of the case over the phone with someone who is in jail. Jail calls are recorded and we have seen too many cases go south based on remarks made over recorded lines.</p></div>
    </div>
  </section>

  <section class="step step--reports">
    <div class="step__icon"><div class="step__art" role="img" aria-label="Police report under a magnifying glass"></div></div>
    <div class="step__panel">
      <h2 class="step__title"><span class="step__num">05</span>Police Reports and Discovery</h2>
      <div class="step__text"><p>We will do our best to provide you with copies of everything we receive on your case. Most information will be emailed, so please keep your email ad&shy;dress up to date.</p></div>
    </div>
  </section>

  <section class="step step--contact step--flip">
    <div class="step__icon"><div class="step__art" role="img" aria-label="Documents and phone book with an update badge"></div></div>
    <div class="step__panel">
      <h2 class="step__title"><span class="step__num">06</span>Changes in Contact Information</h2>
      <div class="step__text"><p>If you move or change numbers during the case, please let us know. It is diffi&shy;cult to help if we are unable to reach you, and helping you is why we are here.</p></div>
    </div>
  </section>

  <section class="step step--court">
    <div class="step__icon"><div class="step__art" role="img" aria-label="Judge's gavel"></div></div>
    <div class="step__panel">
      <h2 class="step__title"><span class="step__num">07</span>Court Appearances</h2>
      <div class="step__text"><p>Cases do not get resolved as quickly as they do on television. Expect there to be several hearings in your case and it may be necessary for you to attend one or more of them. If a hearing is set, you will receive notice of the date and time of each hearing.</p></div>
    </div>
  </section>

  <section class="step step--billing step--flip">
    <div class="step__icon"><div class="step__art" role="img" aria-label="Client with a speech bubble and a dollar bill"></div></div>
    <div class="step__panel">
      <h2 class="step__title"><span class="step__num">08</span>Billing and Collections</h2>
      <div class="step__text"><p>We understand that this investment was a huge decision for you. As we focus on providing the best representation, we will need for you to stay on schedule with any payment arrangements agreed to at the time of your initial consulta&shy;tion.</p></div>
    </div>
  </section>

</main>
</body>
</html>
```